Menu Design for Indian Restaurant

We are a new Indian restaurant, named Spices of Sarani Restaurant, looking for a sophisticated looking menu. It is a semi-formal dining restaurant with wooden tables and chairs and will have a focus on a creating a lively atmosphere. Environment-friendly products will be used, and the menu will be 100% vegetarian. There will be an emphasis on fresh, healthy and delicious food. We will be targeting vegans, vegetarians, health conscious people, people from all age groups, Indians, Australian's as well as other ethnic communities. We need a clean, simple, sophisticated design for the new restaurant menu. Attached is the restaurant logo for reference.

UPDATE:
- We have attached the menu
- We are not looking for any particular type of layout or size (open to suggests). Please suggest this after having a look at the menu contents. However, we will be having one formal menu to be used in the restaurant, and one in brochure form for distribution.
- There are no images at present. If you feel the need of images, please use sample images for now.

Thank you for the entries thus far.
Updates

Target Market(s)

All age groups from different nationalities

Industry/Entity Type

Indian Restaurant

Colors

Designer to choose colors to be used in the design.

Requirements
Nice to have
• This will be printed on environmentally friendly paper.

```html
<!DOCTYPE html>
<html lang="en">
<head>
<meta charset="utf-8">
<title>Mains Menu</title>
<link href="https://fonts.googleapis.com/css2?family=Oswald:wght@400&family=Roboto:wght@300;500&display=swap" rel="stylesheet">
<style>
  :root{
    --green:#1f8a3c;
    --green-deep:#15702e;
    --green-line:#2d5a2a;
    --paper-light:#f6f6f6;
    --paper-dark:#e2e2e2;
    --ink:#222222;
    --ink-soft:#555555;
    --cream:#ffffff;
    --cream-soft:#dcefdf;
  }
  html,body{margin:0;padding:0;overflow:hidden;background:#fff;}
  .menu-page{position:relative;width:848px;height:1200px;overflow:hidden;font-family:"Roboto",sans-serif;}
  .backdrop{position:absolute;inset:0;}
  .section-title{position:absolute;left:336px;top:44px;width:176px;text-align:center;
    font-family:"Oswald",sans-serif;font-weight:400;font-size:60px;line-height:1;color:var(--ink);letter-spacing:-1px;margin:0;}
  .dish-list{position:absolute;top:283px;margin:0;padding:0;list-style:none;}
  .dish-list--left{left:42px;width:330px;}
  .dish-list--right{left:474px;width:340px;}
  .dish{height:40px;}
  .dish__name{font-weight:500;font-size:12.5px;letter-spacing:.3px;text-transform:uppercase;line-height:15px;display:block;}
  .dish__desc{font-weight:300;font-size:10.5px;line-height:12.5px;display:block;padding-left:18px;margin-top:4px;}
  .dish-list--left .dish__name{color:var(--cream);}
  .dish-list--left .dish__desc{color:var(--cream-soft);}
  .dish-list--right .dish__name{color:#3a3a3a;}
  .dish-list--right .dish__desc{color:var(--ink-soft);}
  .dish--tight .dish__desc{margin-top:0;}
</style>
</head>
<body>
<main class="menu-page">
  <svg class="backdrop" width="848" height="1200" viewBox="0 0 848 1200">
    <defs>
      <linearGradient id="paper" x1="0" y1="0" x2="1" y2="1">
        <stop offset="0" stop-color="var(--paper-dark)"/>
        <stop offset=".5" stop-color="var(--paper-light)"/>
        <stop offset="1" stop-color="var(--paper-dark)"/>
      </linearGradient>
      <linearGradient id="leafGreen" x1="0" y1="0" x2="0" y2="1">
        <stop offset="0" stop-color="var(--green)"/>
        <stop offset="1" stop-color="var(--green-deep)"/>
      </linearGradient>
      <linearGradient id="grillTones" x1="0" y1="0" x2="1" y2="1">
        <stop offset="0" stop-color="#b34a2c"/>
        <stop offset=".45" stop-color="#8a7a3a"/>
        <stop offset="1" stop-color="#4c3f26"/>
      </linearGradient>
      <linearGradient id="sandwichTones" x1="0" y1="0" x2="1" y2="1">
        <stop offset="0" stop-color="#3b3a38"/>
        <stop offset=".5" stop-color="#8b6a45"/>
        <stop offset="1" stop-color="#2d2c2b"/>
      </linearGradient>
      <linearGradient id="curryTones" x1="0" y1="0" x2="1" y2="1">
        <stop offset="0" stop-color="#c7321f"/>
        <stop offset=".6" stop-color="#d8652e"/>
        <stop offset="1" stop-color="#3a2c26"/>
      </linearGradient>
    </defs>
    <rect x="424" y="0" width="424" height="1200" fill="url(#paper)"/>
    <rect x="0" y="0" width="424" height="1200" fill="url(#leafGreen)"/>
    <path role="img" aria-label="Photo of grilled vegetables and paneer on a white plate" d="M0 0H424V205Q212 214 0 236Z" fill="url(#grillTones)"/>
    <path role="img" aria-label="Photo of a wholegrain sandwich with cheese and cress" d="M424 0H848V236Q636 216 424 209Z" fill="url(#sandwichTones)"/>
    <path d="M0 236Q212 214 424 205" fill="none" stroke="#f2f2f2" stroke-width="3"/>
    <path d="M424 209Q636 216 848 236" fill="none" stroke="var(--green-line)" stroke-width="3"/>
    <path role="img" aria-label="Photo of a red vegetable curry in a white bowl" d="M424 1018Q636 1026 848 1044V1200H424Z" fill="url(#curryTones)"/>
    <path d="M424 1018Q636 1026 848 1044" fill="none" stroke="var(--green-line)" stroke-width="3"/>
    <polygon points="336,102 381,27 469,27 512,102 469,178 381,178" fill="#ffffff" fill-opacity=".82"/>
  </svg>

  <h1 class="section-title">MAINS</h1>

  <ul class="dish-list dish-list--left">
    <li class="dish"><span class="dish__name">Paneer Kaliyan 20.9</span><span class="dish__desc">Ricotta cheese cashew nut sultana fry creamy saffron gravy</span></li>
    <li class="dish dish--tight"><span class="dish__name">Awadhi Kofta (4) 21.9</span><span class="dish__desc">Gravy based nuts cream tempered spinach ricotta cheese potatoes dumpling</span></li>
    <li class="dish dish--tight"><span class="dish__name">Paneer Kuchran 19.9</span><span class="dish__desc">Cottage cheese red onion capsicum tomato ginger garlic fresh chilli fresh coriander</span></li>
    <li class="dish"><span class="dish__name">Mattar Paneer 19.9</span><span class="dish__desc">Cottage cheese cubes baby peas onion tomato ginger garlic</span></li>
    <li class="dish"><span class="dish__name">Paneer Pasanda (2pcs) 21.9</span><span class="dish__desc">Cottage cheese sandwich nut creamy gravy ginger garlic</span></li>
    <li class="dish"><span class="dish__name">Palak Paneer 19.9</span><span class="dish__desc">Vegetable Momos , yoghurt, ginger , garlic cooked in clay oven</span></li>
    <li class="dish dish--tight"><span class="dish__name">Karahi Paneer 19.9</span><span class="dish__desc">Cottage cheese cubes tossed with capsicum onion tomatoes coriander seeds</span></li>
    <li class="dish"><span class="dish__name">Pindi Chana6.9</span><span class="dish__desc">Chickpeas onion tomato green chilli lemon ginger</span></li>
    <li class="dish"><span class="dish__name">Dal Tarka 15.9</span><span class="dish__desc">Yellow split peas onion tomato ginger garlic</span></li>
    <li class="dish"><span class="dish__name">Handi Ki Dal Makhani 15.9</span><span class="dish__desc">Black whole lentil onion tomato ginger cream butter</span></li>
    <li class="dish"><span class="dish__name">Rajmaha Masala 15.9</span><span class="dish__desc">Kidney beans onion ginger garlic fresh coriander tomatoes</span></li>
    <li class="dish dish--tight"><span class="dish__name">Kadi Pakora 16.9</span><span class="dish__desc">Butter milk gram flour mustard curry leafs fresh coriander whole red chilli</span></li>
    <li class="dish"><span class="dish__name">Khumb Hara Piyaz 16.9</span><span class="dish__desc">Mushrooms spring onion ginger garlic tomatoes spice</span></li>
    <li class="dish"><span class="dish__name">Sabzi Tarkari 15.9</span><span class="dish__desc">Mushrooms spring onion ginger garlic tomatoes spice</span></li>
    <li class="dish"><span class="dish__name">Palak Paneer 19.9</span><span class="dish__desc">Cottage cheese baby spinach tomatoes ginger garlic onion cream</span></li>
    <li class="dish"><span class="dish__name">Paneer Tikka Masala 19.9</span><span class="dish__desc">Cottage cheese cubes clay oven cooked onion capsicum tomato</span></li>
    <li class="dish"><span class="dish__name">Gujrati Thali 21.9</span><span class="dish__desc">4 curry salad pickle rice yogurt 2 roti pappadam sweet</span></li>
    <li class="dish"><span class="dish__name">Temil Thali 21.9</span><span class="dish__desc">4 curry salad pickle rice yogurt naan pappadam sweet</span></li>
    <li class="dish"><span class="dish__name">Punjabi Thali 21.9</span><span class="dish__desc">4 curry salad pickle rice yogurt naan pappadam sweet</span></li>
    <li class="dish"><span class="dish__name">Vegetable Chowmein 16.9</span><span class="dish__desc">Singapore noodle capsicum cabbage carrot onion garlic soya chilli</span></li>
    <li class="dish"><span class="dish__name">Chilli Paneer 18.9</span><span class="dish__desc">Cottage cheese capsicum green chilli onion carrots soya chilli sauce</span></li>
    <li class="dish"><span class="dish__name">Chilli Mushrooms 15.9</span><span class="dish__desc">Button mushrooms capsicum red fresh chilli onion soya chilli sauce</span></li>
  </ul>

  <ul class="dish-list dish-list--right">
    <li class="dish"><span class="dish__name">Momos (6) 6.9</span><span class="dish__desc">Vegetables stuffed pastry stemmed chilli sauce</span></li>
    <li class="dish"><span class="dish__name">Cauliflower Manchurian 15.9</span><span class="dish__desc">Battered cauliflower soya and sauce</span></li>
    <li class="dish"><span class="dish__name">Manchurain Veg Balls 16.9</span><span class="dish__desc">Vegetarian ball made with soya and sauce</span></li>
    <li class="dish"><span class="dish__name">Vegetarian Fried Rice 7.9</span><span class="dish__desc">Mix vegetables soya sauce, chili sauce, paneer, tofu</span></li>
    <li class="dish"><span class="dish__name">Chilli Toffu 15.9</span><span class="dish__desc">Tofu fried, fresh green chili, red capsicum, beans sprout, bock choy</span></li>
    <li class="dish"><span class="dish__name">Khumb Mattar 17.9</span><span class="dish__desc">Mushrooms peas tomatoes spice ginger garlic</span></li>
    <li class="dish"><span class="dish__name">Dam Aloo Kasmiri 18.9</span><span class="dish__desc">Stuffed bake potatoes cashew nut sultana coconut in creamy gravy</span></li>
    <li class="dish"><span class="dish__name">Bhindi Do Pyaz 15.9</span><span class="dish__desc">Okra made with onion tomato spice ginger garlic</span></li>
    <li class="dish"><span class="dish__name">Kathal Tarkari (Seasonal) 19.9</span><span class="dish__desc">Fresh jackfruit cooked with tomatoes ginger garlic fresh coriander</span></li>
    <li class="dish"><span class="dish__name">Baingan Bhartha16.9</span><span class="dish__desc">Eggplant pulp tomato fresh coriander ginger garlic</span></li>
    <li class="dish"><span class="dish__name">Paneer Makhani (Nuts) 19.9</span><span class="dish__desc">Cottage cheese cubes butter sauce nuts cream tomato</span></li>
    <li class="dish dish--tight"><span class="dish__name">Sarso Ka Sagg 15.9</span><span class="dish__desc">Fine crushed mustard leafs onion garlic ginger flavoured with mustard oil</span></li>
    <li class="dish"><span class="dish__name">Bagare Baingan (Seasonal) 16.9</span><span class="dish__desc">Baby eggplant spiced stuffed tomato ginger garlic</span></li>
    <li class="dish"><span class="dish__name">Vegetable Korma 16.9</span><span class="dish__desc">Fresh mix vegetable in creamy nut gravy</span></li>
    <li class="dish"><span class="dish__name">Appam Korma 16.9</span><span class="dish__desc">Fresh mix vegetable coconut milk curry leafs mustard</span></li>
    <li class="dish dish--tight"><span class="dish__name">Vendakka 16.9</span><span class="dish__desc">Okra cut, fenugreek seeds, coconut cream, mustard seeds, curry leafs, shallots round</span></li>
    <li class="dish"><span class="dish__name">Bharela Karela 15.9</span><span class="dish__desc">Bitter gourd stuffed potatoes spice onion ginger garlic serve on gravy</span></li>
  </ul>
</main>
</body>
</html>
```